Revamp my web site design

Willowbrook Care Practitioners is a not for profit organisation focused on providing emotional support and counselling services to those with cancer or affected by cancer including those bereaved.

Our web site is intended to welcome suffers to engage with the services of its members and is also provided to encourage additional counsellors to join the organisation and then supports its members with access to materials and courses to extend their professional development.

We have a limited budget and seek to not only improve the attractiveness of the site but also improve the functionality and ease of maintenance. Especially site administrtaion should allow for uploading documents, adding new members, news and events easily.

Existing site is www.willowbrookcare.com.au

```html
<!DOCTYPE html>
<html lang="en">
<head>
<meta charset="utf-8">
<title>Willowbrook Care Practitioners</title>
<link rel="stylesheet" href="https://fonts.googleapis.com/css2?family=EB+Garamond:ital,wght@0,400;0,600;0,700;1,400;1,600&display=swap">
<style>
:root{
  --green:#3fbf0f;
  --green-bright:#5fe01a;
  --green-dark:#1f8c00;
  --grey-band:#cfcfcf;
  --grey-light:#e6e6e6;
  --ink:#111;
  --muted:#8a8a8a;
  --white:#fff;
}
*{box-sizing:border-box;margin:0;padding:0}
html,body{width:1200px;height:2338px;overflow:hidden;background:var(--white)}
body{position:relative;font-family:"EB Garamond",Garamond,serif;color:var(--ink)}
.abs{position:absolute}

/* header */
.brand-mark{left:59px;top:5px;width:172px;height:172px;border-radius:50%;background:var(--green)}
.brand-name{left:240px;top:22px;width:600px;text-align:center;font-size:56px;line-height:64px;color:var(--ink);font-weight:400;letter-spacing:1px}
.tagline{left:280px;top:150px;width:520px;text-align:center;font-style:italic;font-size:21px;color:var(--green)}
.tagline-rule{left:290px;top:188px;width:500px;height:2px;background:var(--green)}
.contact-box{left:877px;top:14px;width:300px}
.contact-box .ask{color:var(--green);font-size:18px;font-weight:600}
.contact-box .phone{color:var(--muted);font-size:16px;line-height:20px;padding-left:10px}
.connect{left:877px;top:96px;display:flex;align-items:center;gap:8px;color:var(--green);font-size:16px}
.connect span.dot{width:34px;height:34px;border-radius:50%;background:#9fb8d4}

/* search */
.search-band{left:53px;top:234px;width:1046px;height:42px;background:var(--grey-band)}
.search-input{left:59px;top:239px;width:180px;height:32px;background:var(--white);display:flex;align-items:center;gap:8px;padding-left:6px;font-size:13px;color:var(--muted)}
.side-tab{left:13px;top:365px;width:14px;height:52px;background:linear-gradient(var(--green),var(--grey-light))}

/* hero */
.hero{left:59px;top:304px;width:1040px;height:432px;background:linear-gradient(90deg,#e9edf0 0%,#f4f4f4 25%,#cfd8d8 45%,#9bc48c 75%,var(--green-bright) 100%)}
.hero-offer{left:865px;top:576px;width:230px;color:var(--white)}
.hero-offer h3{font-style:italic;font-weight:400;font-size:24px;color:var(--ink)}
.hero-offer p{font-size:13px;line-height:21px;font-style:italic}

/* nav */
.main-nav{left:59px;top:736px;width:1040px;height:54px;background:var(--green);display:flex;align-items:center;font-size:19px;font-weight:600}
.main-nav a{color:var(--ink);text-decoration:none;position:absolute;top:14px}
.main-nav .current{left:69px;top:0;width:112px;height:54px;background:var(--white);display:flex;align-items:center;justify-content:center}

/* section banners */
.banner{height:44px;color:var(--white);font-style:italic;font-size:27px;letter-spacing:1px;display:flex;align-items:center;padding-left:22px;background:var(--green);clip-path:polygon(4% 0,100% 0,97% 100%,0 100%)}
.banner::before{content:"";position:absolute}
.band{left:13px;width:1155px;height:48px;background:var(--grey-band);color:var(--white);font-style:italic;font-size:21px;letter-spacing:2px;display:flex;align-items:center;padding-left:200px}

/* screening */
.thumb{top:897px;width:228px;height:135px}
.thumb-1{left:125px;background:linear-gradient(135deg,#1b2e8a,#5e6fd0 50%,#14207a)}
.thumb-2{left:381px;background:linear-gradient(135deg,#7da4cf,#c8483e 55%,#1e4fa3)}
.thumb-3{left:637px;background:linear-gradient(135deg,#f3f3f3,#e6b060 50%,#7c9bd3)}
.thumb-4{left:893px;background:linear-gradient(135deg,#c7421c,#f1863b 50%,#5e1a0c)}
.copy{font-size:14px;line-height:18px;text-align:justify}
.screen-copy{top:1086px;width:228px}

/* what we do */
.col{top:1410px;width:300px}
.col h3{font-size:24px;font-weight:700;font-style:italic;letter-spacing:1px;margin-bottom:6px}
.col h3 em{color:var(--green);font-style:italic}
.read-more{display:flex;gap:4px;margin-top:18px}
.read-more span{background:var(--green);color:var(--ink);font-size:12px;padding:3px 10px;border-radius:10px 2px 10px 2px}

/* team */
.team-photo{left:125px;top:1854px;width:600px;height:247px;background:linear-gradient(180deg,#ffffff 0%,#c9d0d8 40%,#4d6070 75%,#1e2a33 100%)}
.team-quote{left:755px;top:1950px;width:395px}
.team-quote h3{color:var(--green);font-style:italic;font-weight:600;font-size:20px;margin-bottom:6px}

/* footer */
.footer{left:13px;top:2145px;width:1155px;height:160px;background:var(--grey-band)}
.member-form{left:112px;top:2155px;width:240px}
.member-form h4{font-size:19px;font-weight:600;margin-bottom:4px}
.field{width:140px;height:24px;border:2px solid var(--green);background:var(--white);font-size:12px;padding-left:4px;color:var(--green);margin-bottom:6px;line-height:20px}
.btn{display:inline-block;background:var(--green);color:var(--white);font-size:13px;font-weight:600;letter-spacing:1px;padding:3px 22px;border-radius:12px}
.join-art{left:610px;top:2150px;width:240px;height:155px;background:linear-gradient(90deg,rgba(255,255,255,0),#bff09a 40%,var(--green) 70%,rgba(207,207,207,0))}
.join{left:848px;top:2215px;font-size:17px;line-height:20px}
.copyright{left:13px;top:2306px;width:1155px;height:32px;background:var(--green-dark);color:var(--white);font-size:17px;padding-left:112px;display:flex;align-items:center;gap:6px}
</style>
</head>
<body>

<header>
  <div class="abs brand-mark"></div>
  <h1 class="abs brand-name">Willowbrook Care<br>Practitioners</h1>
  <p class="abs tagline">Death is not yet your loved one still needs you...</p>
  <div class="abs tagline-rule"></div>
  <div class="abs contact-box">
    <p class="ask">Need counselling services?</p>
    <p class="phone">Call 082 555 014 27</p>
    <p class="phone">082 555 093 61</p>
  </div>
  <div class="abs connect">Connect to us <span class="dot"></span><span class="dot"></span><span class="dot"></span></div>
</header>

<div class="abs search-band"></div>
<div class="abs search-input">
  <svg width="26" height="20" viewBox="0 0 26 20"><circle cx="16" cy="8" r="6" fill="none" stroke="#3fbf0f" stroke-width="3"/><line x1="11" y1="12" x2="3" y2="18" stroke="#3fbf0f" stroke-width="3"/></svg>
  Search...
</div>
<div class="abs side-tab"></div>

<div class="abs hero" role="img" aria-label="Photo of two smiling women, one a doctor in a white coat with stethoscope and clipboard"></div>
<div class="abs hero-offer">
  <h3>What we have for you</h3>
  <p>Lorem ipsum dolor sit amet, consectetuer adipiscing elit, sed diam nonummy nibh euismod tincidunt ut laoreet dolore magna aliquam erat volutpat. Ut wisi enim ad minim veniam, quis nostrud exerci tation.</p>
</div>

<nav class="abs main-nav">
  <a class="current" href="#">Home</a>
  <a href="#" style="left:229px">About</a>
  <a href="#" style="left:362px">Our Services</a>
  <a href="#" style="left:514px">Events</a>
  <a href="#" style="left:645px">Members</a>
  <a href="#" style="left:778px">News</a>
  <a href="#" style="left:890px">Contact</a>
</nav>

<h2 class="abs banner" style="left:107px;top:822px;width:480px">Cancer Screening &amp; Diagnosis</h2>
<div class="abs thumb thumb-1" role="img" aria-label="Blue laboratory pipette tips"></div>
<div class="abs thumb thumb-2" role="img" aria-label="Blood sample tubes in a rack"></div>
<div class="abs thumb thumb-3" role="img" aria-label="Medicine bottles and pills"></div>
<div class="abs thumb thumb-4" role="img" aria-label="Laboratory glassware in red light"></div>
<p class="abs copy screen-copy" style="left:125px">Lorem ipsum dolor sit amet, consectetuer adipiscing elit, sed diam nonummy nibh euismod tincidunt ut laoreet dolore magna aliquam erat volutpat. Ut wisi enim ad minim veniam, quis nostrud exerci tation ullamcorper suscipit lobortis nisl ut aliquip aliqui.</p>
<p class="abs copy screen-copy" style="left:381px">Lorem ipsum dolor sit amet, consectetuer adipiscing elit, sed diam nonummy nibh euismod tincidunt ut laoreet dolore magna aliquam erat volutpat. Ut wisi enim ad minim veniam, quis nostrud exerci tation ullamcorper suscipit lobortis nisl ut aliquip aliqui.</p>
<p class="abs copy screen-copy" style="left:637px">Lorem ipsum dolor sit amet, consectetuer adipiscing elit, sed diam nonummy nibh euismod tincidunt ut laoreet dolore magna aliquam erat volutpat. Ut wisi enim ad minim veniam, quis nostrud exerci tation ullamcorper suscipit lobortis nisl ut aliquip aliqui.</p>
<p class="abs copy screen-copy" style="left:893px">Lorem ipsum dolor sit amet, consectetuer adipiscing elit, sed diam nonummy nibh euismod tincidunt ut laoreet dolore magna aliquam erat volutpat. Ut wisi enim ad minim veniam, quis nostrud exerci tation ullamcorper suscipit lobortis nisl ut aliquip aliqui.</p>

<div class="abs band" style="top:1240px">We take you through in every step of your counselling.....</div>

<h2 class="abs banner" style="left:107px;top:1330px;width:440px">What we do for you</h2>
<section class="abs col" style="left:125px">
  <h3>What is counselling<em>?</em></h3>
  <p class="copy">Lorem ipsum dolor sit amet, consectetuer adipiscing elit, sed diam nonummy nibh euismod tincidunt ut laoreet dolore magna aliquam erat volutpat. Ut wisi enim ad minim veniam, quis nostrud exerci tation ullamcorper suscipit lobortis nisl ut aliquip aliqui Lorem ipsum dolor sit amet, consectetuer adipiscing elit, sed diam no nummy nibh euismod tincidunt ut</p>
  <div class="read-more"><span>Read</span><span>more</span></div>
</section>
<section class="abs col" style="left:483px">
  <h3>How will it help me<em>?</em></h3>
  <p class="copy">Lorem ipsum dolor sit amet, consectetuer adipiscing elit, sed diam nonummy nibh euismod tincidunt ut laoreet dolore magna aliquam erat volutpat. Ut wisi enim ad minim veniam, quis nostrud exerci tation ullamcorper suscipit lobortis nisl ut aliquip aliqui Lorem ipsum dolor sit amet, consectetuer adipiscing elit, sed diam no nummy nibh euismod tincidunt ut</p>
  <div class="read-more"><span>Read</span><span>more</span></div>
</section>
<section class="abs col" style="left:835px">
  <h3>Why cancer counselling<em>?</em></h3>
  <p class="copy">Lorem ipsum dolor sit amet, consectetuer adipiscing elit, sed diam nonummy nibh euismod tincidunt ut laoreet dolore magna aliquam erat volutpat. Ut wisi enim ad minim veniam, quis nostrud exerci tation ullamcorper suscipit lobortis nisl ut aliquip aliqui Lorem ipsum dolor sit, consectetuer adipiscing elit, sed diam no nummy nibh euismod tincidunt ut</p>
  <div class="read-more"><span>Read</span><span>more</span></div>
</section>

<div class="abs band" style="top:1680px">How to access our Counselling Services....</div>

<h2 class="abs banner" style="left:107px;top:1791px;width:440px">Our counselling team</h2>
<div class="abs team-photo" role="img" aria-label="Illustration of grey figures seated in chairs around a group meeting"></div>
<section class="abs team-quote">
  <h3>"cancer is not the end of everything"</h3>
  <p class="copy">Lorem ipsum dolor sit amet, consectetuer aiscing elit, sed diam nonummy nibh euismo ncidunt ut laoreet dolore magna aliquam erat volutpat. Ut wisi enim ad minim veniam, quisitrud exerci tation ullamcorper suscipit lobortis nisl ut aliquip aliqui Lorem ipsum dolor sit, consectetuer adipiscing elit, sed diam no ny nibh euismod tincidunt ut Lorem ipsum dolor sit amet, consectetuer aiscing elit, sed diam nonummy nibh euismod tincidunt ut laoreet dolore magna aliquam erat volutpat. Ut wisi enim ad minim veniam, quisitrud.</p>
</section>

<footer>
  <div class="abs footer"></div>
  <div class="abs member-form">
    <h4>Become a member</h4>
    <div class="field">Name</div>
    <div class="field">Phone number</div>
    <div class="field">Email</div>
    <span class="btn">SUBMIT</span>
  </div>
  <div class="abs join-art" role="img" aria-label="Green profile silhouettes of heads facing right"></div>
  <div class="abs join">
    <p>Are you a counsellor?</p>
    <p>you can join our counsell team</p>
    <span class="btn" style="margin-top:8px">SIGN UP</span>
  </div>
  <div class="abs copyright">
    <svg width="16" height="16" viewBox="0 0 16 16"><circle cx="8" cy="8" r="7" fill="none" stroke="#fff" stroke-width="1.5"/><path d="M10.5 5.5a3.3 3.3 0 1 0 0 5" fill="none" stroke="#fff" stroke-width="1.5"/></svg>
    Copyright 2013.All Rights Reserved
  </div>
</footer>

</body>
</html>
```